Bramblewood Outings brochure

We need a brochure designed that is modern, high impact and grabs potential customers attention. I have provided a draft mock brochure as an example and to provide the desired information. The lay out and design can be changed.

The front to include image (examples provided. I may provide other images if I can source) Logo, Joining the Community, and perhaps a Community Access and Lifestyle Support Service, Specialising in Lifestyle and Recreation

Refer to website for information on the service www.bramblewoodoutings.com.au

Use colours of logo for design

Target Market(s)

CWPA participants (People with a disability and their family)

Colors

Designer to choose colors to be used in the design.

Requirements
Must have
• Image/s of people, logo, text in mock up design. Example images provided. Will source more images and upload.
Nice to have
• More than one image

```html
<!DOCTYPE html>
<html lang="en">
<head>
<meta charset="utf-8">
<title>Bramblewood Outings – Brochure</title>
<link href="https://fonts.googleapis.com/css2?family=Arimo:wght@400;700&display=swap" rel="stylesheet">
<style>
  :root {
    --green-deep: #3a9e6c;
    --green-mid: #52bf92;
    --green-light: #cdeee0;
    --teal-accent: #3bb58a;
    --ink: #111;
    --paper: #fff;
    --frame: #2f7f58;
  }
  html, body { margin: 0; padding: 0; overflow: hidden; }
  body { width: 1200px; height: 848px; font-family: 'Arimo', Arial, sans-serif; color: var(--ink); }
  .brochure {
    position: relative; width: 1200px; height: 848px; overflow: hidden;
    background:
      radial-gradient(ellipse 260px 230px at 610px 540px, var(--green-light) 0%, rgba(205,238,224,0) 100%),
      linear-gradient(180deg, var(--green-mid) 0%, #4fbb8c 50%, var(--green-deep) 100%);
    box-shadow: inset 0 0 0 2px var(--frame);
  }
  .section-title {
    position: absolute; margin: 0; font-size: 29px; font-weight: 700; letter-spacing: 0.2px; line-height: 1;
  }
  .panel {
    position: absolute; background: var(--paper); box-sizing: border-box;
    border: 1px solid #cfd8d3; box-shadow: -2px -2px 0 #2a7d55 inset, 2px 2px 3px rgba(0,0,0,.35);
    font-size: 19px; line-height: 24px;
  }
  .panel p { margin: 0; }
  .panel ul { margin: 0; padding: 0; list-style: none; }
  .who-are-we { left: 46px; top: 102px; width: 362px; height: 133px; padding: 10px 10px 0 12px; }
  .who-we-assist { left: 46px; top: 294px; width: 362px; height: 303px; padding: 10px 8px 0 12px; }
  .who-we-assist li { position: relative; }
  .who-we-assist li.dot::before { content: "•"; position: absolute; left: -10px; }
  .role { left: 46px; top: 646px; width: 402px; height: 111px; padding: 11px 8px 0 13px; }
  .philosophy { left: 437px; top: 102px; width: 346px; height: 395px; padding: 0 6px 0 14px; }
  .value-title {
    display: block; text-align: center; color: var(--teal-accent); font-weight: 700;
    font-size: 20px; letter-spacing: 1px; margin: 4px 0 2px;
  }
  .philosophy p { margin-bottom: 8px; }
  .assist { left: 813px; top: 102px; width: 373px; height: 587px; padding: 4px 4px 0 19px; font-size: 17.6px; line-height: 22.3px; }
  .assist ul { margin-top: 22px; }
  .assist li { position: relative; }
  .assist li::before { content: "•"; position: absolute; left: -14px; }
  .assist .closing { margin-top: 22px; }
  .apply { left: 813px; top: 736px; width: 373px; height: 57px; padding: 6px 4px 0 19px; font-size: 17.6px; line-height: 22.3px; }
  .chair-image {
    position: absolute; left: 500px; top: 508px; width: 232px; height: 236px; border-radius: 12px;
    background: radial-gradient(circle at 50% 55%, #5b4a8c 0%, #2c2a3a 55%, rgba(44,42,58,0) 75%);
    opacity: .85;
  }
  .brand { position: absolute; left: 470px; top: 742px; display: flex; align-items: center; gap: 14px; }
  .brand-dot { width: 46px; height: 46px; border-radius: 50%; background: var(--paper); }
  .brand-name { color: var(--paper); font-size: 33px; font-weight: 700; line-height: 38px; width: 220px; }
</style>
</head>
<body>
<main class="brochure">
  <h2 class="section-title" style="left:58px;top:67px;">WHO ARE WE</h2>
  <section class="panel who-are-we">
    <p>A family driven lifestyle, recreation and leisure support service operated by a management committee consisting of parents and interested community members.</p>
  </section>

  <h2 class="section-title" style="left:58px;top:254px;">WHO WE ASSIST</h2>
  <section class="panel who-we-assist">
    <p>People with a disability who:</p>
    <ul style="margin-top:24px;">
      <li class="dot">Are over the age of 16 years ;</li>
      <li>Reside in the Tallowmere region, from</li>
      <li class="dot">Fernbrook to Shell Bay;</li>
      <li class="dot">meet the Northland Disability services eligibility criteria;</li>
      <li class="dot">are registered as Community Wellbeing Plan (CWPA) participants after rollout in Tallowmere in July 2018; and/or</li>
      <li>have their own finacial resources.</li>
    </ul>
  </section>

  <h2 class="section-title" style="left:58px;top:613px;">ROLE OF FAMILY/ADVOCATE</h2>
  <section class="panel role">
    <p>Families are our greatest resource and we actively seek their input to help the person with a Disability maximize choice and control over their own lives.</p>
  </section>

  <h2 class="section-title" style="left:452px;top:67px;">OUR PHILOSOPHY</h2>
  <section class="panel philosophy">
    <span class="value-title">CHOICE</span>
    <p>Choice is a key element in lifestyle, recreation and lifestyle pursuits, and we tailor support that meet people’s personal plans and goals.</p>
    <span class="value-title" style="margin-top:14px;">INCLUSION</span>
    <p>We believe that supporting people individually is the best way to enable them to attain a valued role in their community.</p>
    <span class="value-title" style="margin-top:14px;">OPPORTUNITY</span>
    <p>All people have the right to be part of their community and to experience life’s opportunities.</p>
  </section>

  <h2 class="section-title" style="left:833px;top:67px;">HOW WE ASSIST</h2>
  <section class="panel assist">
    <p>We assist people to:</p>
    <ul>
      <li>Plan what support they need;</li>
      <li>Choose suitable support people;</li>
      <li>Accomplish daily living activities;</li>
      <li>Participate in social and community activities;</li>
      <li>Enhance and maintain independence, self confidence and self esteem;</li>
      <li>Build capacity and improve or maintain skills;</li>
      <li>Keep a job by supporting people in the work place;</li>
      <li>Improve lifelong learning;</li>
      <li>Maintain health and wellbeing and achieve their goals and desired outcomes;</li>
      <li>We employ support people to assist individuals on a one to one ratio;</li>
      <li>In their home and in generic community settings;</li>
      <li>To implement their personal plan;</li>
      <li>To access community services and to meet their changing needs;</li>
    </ul>
    <p class="closing">We can provide 24 hour support but all support is in non-segregated settings.</p>
  </section>

  <h2 class="section-title" style="left:833px;top:704px;">HOW TO APPLY</h2>
  <section class="panel apply">
    <p>Please contact our office to discuss how bramblewood outings can support you.</p>
  </section>

  <div class="chair-image" role="img" aria-label="Photo of a lightweight manual wheelchair with purple frame"></div>

  <div class="brand">
    <span class="brand-dot"></span>
    <span class="brand-name">Bramblewood Outings</span>
  </div>
</main>
</body>
</html>
```